KVTA Promo Flyer for Corporate Events

Need a 8 page company overview

Target Market(s)

Creditors and Service Providers

Industry/Entity Type

Credit Card

Font styles to use
Serif

Colors
0455a3
fbf289

Requirements
Must have
• Fantastic Material and Creative
Nice to have
• Creative and personal

```html
<!DOCTYPE html>
<html lang="en">
<head>
<meta charset="utf-8">
<title>KVTA Company Overview – Leadership</title>
<link rel="stylesheet" href="https://fonts.googleapis.com/css2?family=Lato:wght@400;700&display=swap">
<style>
  :root {
    --backdrop: #c4c4c4;
    --page-blue-deep: #0455a3;
    --page-blue-light: #0a6cba;
    --heading-yellow: #fbf289;
    --marker-gold: #fbb91f;
    --band-start: #f9b417;
    --band-end: #fbf289;
    --body-text: #ffffff;
  }
  * { margin: 0; padding: 0; box-sizing: border-box; }
  html, body {
    width: 960px;
    height: 1200px;
    overflow: hidden;
    background: var(--backdrop);
  }
  .page {
    position: absolute;
    left: 57px;
    top: 0;
    width: 846px;
    height: 1200px;
    background: linear-gradient(160deg, var(--page-blue-deep) 0%, #0660ae 55%, var(--page-blue-light) 100%);
    font-family: 'Lato', sans-serif;
    color: var(--body-text);
    overflow: hidden;
  }
  .profile {
    position: absolute;
    left: 38px;
    width: 770px;
  }
  .profile-name {
    position: relative;
    padding-left: 25px;
    font-size: 23px;
    font-weight: 700;
    line-height: 28px;
    color: var(--heading-yellow);
  }
  .profile-name::before {
    content: "";
    position: absolute;
    left: 0;
    top: 1px;
    width: 13px;
    height: 27px;
    background: var(--marker-gold);
  }
  .profile-role {
    position: absolute;
    left: 25px;
    font-size: 21px;
    font-weight: 400;
    color: var(--heading-yellow);
    line-height: 26px;
  }
  .profile-text {
    position: absolute;
    left: 0;
    width: 770px;
    font-size: 16.8px;
    line-height: 22px;
    text-align: justify;
  }
  .accent-band {
    position: absolute;
    left: 0;
    bottom: 2px;
    width: 100%;
    height: 11px;
    background: linear-gradient(90deg, var(--band-start), var(--band-end));
  }
</style>
</head>
<body>
  <main class="page">
    <section class="profile" style="top:39px">
      <h2 class="profile-name">Daniel Marlowe II</h2>
      <p class="profile-role" style="top:32px">Chief Financial Offier</p>
      <p class="profile-text" style="top:91px">Daniel KVTA in 2009. He is directly resposbilile for KVTA’s finance and compliance. Among his responsibilities, he oversees bookkeeping and trust account reconciliation, analyzes credit statistics capital structure, and other financial information.</p>
      <p class="profile-text" style="top:173px">Daniel bgain his career in finance in 2005 with Harbor Crest Securities in New York as in investment banking analayst. In 2006 he joined Aldren Vale Asset Management as a Hedge Fund Analyst in Distressed Credit Strategies. He hold’s a bachelor of ARTS degree in Economics from Westbrook College in Westbrook, VT.</p>
    </section>

    <section class="profile" style="top:372px">
      <h2 class="profile-name">Bradley Ross Marlowe</h2>
      <p class="profile-text" style="top:51px">Bradley joined KVTA in 2002 first as a collector and then as a sales represented. He was promoted to his current role in 2006 where he oversees all collections activity. Bradley responsibilities include: recruiting, training, and managing all collection associations/</p>
      <p class="profile-text" style="top:131px">Bradley also manages all hardware, software, and outbound call functions. He builds and manages account flow procedures within collection software as well as audits collection files. In addition, he listens to call recordings with collection representatives to ensure quality and compliance.</p>
    </section>

    <section class="profile" style="top:644px">
      <h2 class="profile-name">Susan Harlan</h2>
      <p class="profile-text" style="top:56px">Susan joined KVTA in 2018 bringing over 20 years of management and executive experience in servicebased industries; Susan holds a Bachelor of Arts in Business Administration from Pinecrest University of Tacoma, Washington.</p>
      <p class="profile-text" style="top:137px">Susan is responsible for ensuring the integration of key initiatives company wide. Including those for administration, client services, sales, marketing, recruiting, retention, and compliance. She is respomsible for process improvement and proactively develops systems designed to maximize business efficiency.</p>
    </section>

    <section class="profile" style="top:945px">
      <h2 class="profile-name">Stella Whitford</h2>
      <p class="profile-text" style="top:52px">Stella joined KVTA in 1998 and has been instrumental in the growth and development of the company. Stella works directly with clients to answer day-to-day questions about accounts. Including providing statements, connectivity, with our client site, and information about specific accounts.</p>
      <p class="profile-text" style="top:156px">Stella oversees all administrative functions of the company for client’s services. She is also able to initiate requests for customized reporting or other special projects</p>
    </section>

    <div class="accent-band"></div>
  </main>
</body>
</html>
```